Cafe / catering Flyer

We are a higher end Industrial Cafe, located between factorys across from the postoffice in Campbellfield. I would like the following information on my flyer

Wexford Lane Cafe
Address: 14 Brindle St, Campbellfield 3061 (Across from Post Office)
Ph: 9417 6281
Email:wexlanecafe@mailbrook.com
Like us on Facebook: Wexford Lane Cafe
Download our App: Wexford Lane Cafe
Trading hours: Mon to Fri 5:30am to 4pm And Sat 7am to 1pm.
Amazing Breakfast Menu and even better Lunch menu!! Eat in or Takeaway
Daily CHEF made meals, Foccacias and wraps, fresh sandwich bar and fresh salads.
Best cafe in Campbellfield!!
Free local deliveries for orders over $50.
Daily Milk and paper deliveries to offices in the local area.
Free WIFI

The main purpose of the flyer is to pick up new big corporate customers that will hopefully take advantage of our catering services delivered to their office. I want to see a big emphasis made on the following :

CATERING CATERING CATERING!!
Delicious Fresh food delivered straight to your office. We cater for any function, or meeting. No Job too big or too Small

We offer a massive range from simple platters to a full ROAST BUFFET.
We Guarantee to impress
20% OFF FOR FIRST TIME CATERING CUSTOMERS!!
Contact us today to see what we can do for you.

Target Market(s)

corporate customers in the local area.

Industry/Entity Type

Cafe

Requirements
Must have
• Must have a big emphasis on Catering. I would like to pick up customers fro this side of the business
Nice to have
• dot points
• straight to the point
Should not have
• too much writing

```html
<!DOCTYPE html>
<html lang="en">
<head>
<meta charset="utf-8">
<title>Wexford Lane Cafe – Flyer</title>
<link href="https://fonts.googleapis.com/css2?family=Arvo:wght@400;700&family=Josefin+Slab:wght@400;600;700&family=Open+Sans:wght@400;600&display=swap" rel="stylesheet">
<style>
:root{
  --bg:#e6e6e6;
  --board:#232323;
  --board-light:#2f2f2f;
  --orange:#f39a1e;
  --orange-dark:#d9780c;
  --white:#ffffff;
  --muted:#bdbdbd;
}
*{margin:0;padding:0;box-sizing:border-box}
html,body{width:1200px;height:799px;overflow:hidden}
body{background:radial-gradient(circle at 50% 40%,#f4f4f4,#cfcfcf);font-family:'Arvo',serif;color:var(--white);position:relative}
.flyer{position:absolute;top:32px;width:520px;height:735px;background:repeating-linear-gradient(90deg,var(--board) 0 60px,var(--board-light) 60px 62px,#262626 62px 124px);overflow:hidden;box-shadow:0 6px 18px rgba(0,0,0,.35)}
.flyer--menu{left:60px}
.flyer--front{left:620px}
.flyer svg.shapes{position:absolute;inset:0}
.abs{position:absolute}

/* front */
.brand{left:360px;top:60px;width:150px;text-align:center}
.brand__mark{width:64px;height:64px;border-radius:50%;border:5px solid var(--orange);margin:0 auto 8px}
.brand__name{font-weight:700;font-size:13px;line-height:1.15;text-transform:uppercase}
.headline{right:22px;top:200px;text-align:right;font-family:'Josefin Slab',serif;font-weight:600;font-size:34px;line-height:1.05}
.headline em{font-style:normal;color:var(--orange)}
.badge{left:48px;top:327px;width:110px;height:110px;text-align:center;display:flex;flex-direction:column;justify-content:center;font-size:11px;line-height:1.15;font-weight:700}
.badge strong{font-size:17px}
.intro{left:28px;top:470px;width:280px;font-size:14px;line-height:1.45}
.contact{left:28px;top:655px;width:250px;font-size:12px;line-height:1.45}
.contact__phone{display:flex;align-items:center;gap:8px;font-size:19px;font-weight:700;color:var(--orange);margin-bottom:5px}
.icon{width:20px;height:20px;flex:none}
.details{left:290px;top:655px;width:210px;font-size:11px;line-height:1.45;text-align:right}
.details h4{font-size:12px;color:var(--orange);font-weight:700}

/* menu side */
.catering{left:38px;top:56px;width:170px;height:170px;display:flex;flex-direction:column;align-items:center;justify-content:center;text-align:center;font-size:11px;line-height:1.3;padding:14px}
.catering strong{font-size:22px;letter-spacing:1px;line-height:1.1;margin-bottom:5px}
.range{left:28px;top:250px;width:470px;font-size:13px;line-height:1.45}
.menu-title{left:28px;top:296px;font-size:22px;font-weight:700;color:var(--orange)}
.menu-col{width:220px;font-family:'Open Sans',sans-serif;font-size:10px;line-height:1.4;color:var(--muted)}
.menu-col--left{left:28px;top:334px}
.menu-col--right{left:272px;top:334px}
.menu-group h3{font-family:'Arvo',serif;font-size:13px;color:var(--white);border-bottom:1px solid #666;padding-bottom:3px;margin-bottom:4px}
.menu-group{margin-bottom:10px}
.menu-group li{list-style:none;display:flex;justify-content:space-between}
.promo{left:28px;top:642px;width:220px;height:68px;background:var(--orange);border:3px solid var(--white);display:flex;flex-direction:column;justify-content:center;text-align:center;font-size:11px;font-weight:700;line-height:1.25}
.promo strong{font-size:20px}
.order{left:272px;top:652px;width:230px}
.order p{font-size:13px;font-weight:700;margin-bottom:6px}
</style>
</head>
<body>

<section class="flyer flyer--menu">
  <svg class="shapes" width="520" height="735" viewBox="0 0 520 735">
    <defs>
      <linearGradient id="lasagnaTone" x1="0" y1="0" x2="1" y2="1">
        <stop offset="0" stop-color="#d9c39a"/><stop offset=".5" stop-color="#b8702e"/><stop offset="1" stop-color="#6e8c3a"/>
      </linearGradient>
    </defs>
    <path d="M0 0H520V120Q300 150 150 230Q70 250 0 230Z" fill="url(#lasagnaTone)" role="img" aria-label="Photo of a plated lasagne with side salad"/>
    <path d="M0 232Q70 252 150 232Q300 152 520 122" fill="none" stroke="var(--orange)" stroke-width="8"/>
    <circle cx="123" cy="141" r="92" fill="var(--orange)" stroke="var(--white)" stroke-width="4"/>
  </svg>
  <div class="abs catering"><strong>CATERING</strong>Fresh food delivered to your office. Any function, no job too big or too small.</div>
  <p class="abs range">We have a wide range of options from simple sandwich platters to a full roast buffet.</p>
  <h2 class="abs menu-title">Our Menu</h2>

  <div class="abs menu-col menu-col--left">
    <div class="menu-group"><h3>Foccacia</h3><ul>
      <li><span>Vegetarian</span><span>8.00</span></li>
      <li><span>Pizza Style</span><span>8.00</span></li>
      <li><span>Hawaiian</span><span>8.00</span></li>
      <li><span>Gourmet Smoked Salmon</span><span>8.00</span></li>
      <li><span>or Your Choice of Fillings</span><span></span></li>
    </ul></div>
    <div class="menu-group"><h3>Breakfast</h3><ul>
      <li><span>Egg &amp; Bacon S/W</span><span>4.50</span></li>
      <li><span>Egg &amp; Bacon Roll</span><span>5.00</span></li>
      <li><span>Egg Bacon &amp; Cheese S/W</span><span>5.00</span></li>
      <li><span>Egg Bacon &amp; Cheese Roll</span><span>5.50</span></li>
      <li><span>Big Breakfast</span><span>12.00</span></li>
    </ul></div>
    <div class="menu-group"><h3>Sweets</h3><ul>
      <li><span>Donuts</span><span>2.50</span></li>
      <li><span>Fruit Cakes</span><span>4.50</span></li>
      <li><span>Asst. Slices</span><span>3.50</span></li>
      <li><span>Muffins</span><span>3.50</span></li>
    </ul></div>
  </div>

  <div class="abs menu-col menu-col--right">
    <div class="menu-group"><h3>Hot Food</h3><ul>
      <li><span>Grilled S/W</span><span>5.00</span></li>
      <li><span>Roast Meat S/W</span><span>7.50</span></li>
      <li><span>Meat Loaf S/W</span><span>7.00</span></li>
      <li><span>Chicken Kebab</span><span>9.00</span></li>
      <li><span>Plain Hamburger</span><span>6.50</span></li>
      <li><span>Hamburger with the Lot</span><span>9.50</span></li>
      <li><span>Hot Dog</span><span>4.00</span></li>
      <li><span>Pies</span><span>4.50</span></li>
      <li><span>Sausage Roll</span><span>3.50</span></li>
      <li><span>Hot Dog in Batter</span><span>3.50</span></li>
      <li><span>Spring Roll</span><span>2.50</span></li>
      <li><span>Fish</span><span>4.50</span></li>
      <li><span>Dim Sims</span><span>0.90</span></li>
      <li><span>Potato Cakes</span><span>1.50</span></li>
      <li><span>Hash Browns</span><span>1.50</span></li>
      <li><span>Crab Sticks</span><span>1.50</span></li>
      <li><span>Chips</span><span>3.00</span></li>
      <li><span>Wedges</span><span>4.00</span></li>
      <li><span>Pasties</span><span>4.50</span></li>
    </ul></div>
  </div>

  <div class="abs promo"><strong>20% OFF</strong>for first time catering customers</div>

  <div class="abs order">
    <p>Call us to place an order</p>
    <div class="contact__phone">
      <svg class="icon" viewBox="0 0 24 24"><circle cx="12" cy="12" r="10.5" fill="none" stroke="var(--orange)" stroke-width="2"/><path d="M8 6.5l2 0 1 3-1.5 1a7 7 0 0 0 4 4l1-1.5 3 1v2a1.5 1.5 0 0 1-1.5 1.5A10 10 0 0 1 6.5 8 1.5 1.5 0 0 1 8 6.5z" fill="var(--orange)"/></svg>
      <span>+61 3 9417 6281</span>
    </div>
  </div>
</section>

<section class="flyer flyer--front">
  <svg class="shapes" width="520" height="735" viewBox="0 0 520 735">
    <defs>
      <radialGradient id="coffeeTone" cx=".5" cy=".45" r=".6">
        <stop offset="0" stop-color="#f1e2c8"/><stop offset=".45" stop-color="#c87a3a"/><stop offset="1" stop-color="#3a1f16"/>
      </radialGradient>
      <linearGradient id="saladTone" x1="0" y1="0" x2="1" y2="1">
        <stop offset="0" stop-color="#6f9a4a"/><stop offset=".5" stop-color="#e5dd95"/><stop offset="1" stop-color="#8c9a62"/>
      </linearGradient>
      <linearGradient id="traysTone" x1="0" y1="0" x2="1" y2="1">
        <stop offset="0" stop-color="#a0aab0"/><stop offset=".35" stop-color="#8a3f22"/><stop offset="1" stop-color="#5b2414"/>
      </linearGradient>
      <clipPath id="photoBand"><path d="M0 330Q260 265 520 285V610Q430 590 360 500Q300 400 180 380Q80 370 0 400Z"/></clipPath>
    </defs>
    <g clip-path="url(#photoBand)">
      <rect x="0" y="250" width="270" height="380" fill="url(#saladTone)" role="img" aria-label="Photo of a fresh salad bar"/>
      <rect x="270" y="250" width="250" height="380" fill="url(#traysTone)" role="img" aria-label="Photo of catering trays with roast chicken"/>
      <line x1="270" y1="250" x2="270" y2="630" stroke="var(--board)" stroke-width="4"/>
    </g>
    <path d="M0 330Q260 265 520 285" fill="none" stroke="var(--orange)" stroke-width="9"/>
    <path d="M0 400Q80 370 180 380Q300 400 360 500Q430 590 520 610" fill="none" stroke="var(--orange)" stroke-width="6"/>
    <circle cx="150" cy="145" r="132" fill="none" stroke="var(--orange)" stroke-width="10" stroke-dasharray="6 5"/>
    <circle cx="150" cy="145" r="124" fill="var(--orange)"/>
    <circle cx="150" cy="145" r="112" fill="url(#coffeeTone)" role="img" aria-label="Photo of a latte in an orange cup"/>
    <circle cx="103" cy="382" r="58" fill="var(--orange)" stroke="var(--white)" stroke-width="4"/>
    <line x1="0" y1="640" x2="520" y2="640" stroke="var(--orange)" stroke-width="4"/>
  </svg>

  <div class="abs brand">
    <div class="brand__mark"></div>
    <div class="brand__name">Wexford Lane Cafe</div>
  </div>
  <h1 class="abs headline">the <em>best cafe</em><br>in Campbellfield</h1>
  <div class="abs badge"><strong>Free</strong>local deliveries<br>for orders<br>over $50</div>
  <p class="abs intro">We offer an amazing breakfast menu and an even better lunch menu offering hot food, daily special meals, foccacias, fresh salad bar and fresh salads.</p>
  <div class="abs contact">
    <div class="contact__phone">
      <svg class="icon" viewBox="0 0 24 24"><circle cx="12" cy="12" r="10.5" fill="none" stroke="var(--orange)" stroke-width="2"/><path d="M8 6.5l2 0 1 3-1.5 1a7 7 0 0 0 4 4l1-1.5 3 1v2a1.5 1.5 0 0 1-1.5 1.5A10 10 0 0 1 6.5 8 1.5 1.5 0 0 1 8 6.5z" fill="var(--orange)"/></svg>
      <span>+61 3 9417 6281</span>
    </div>
    <p>14 Brindle Street, Campbellfield<br>VIC 3061, Melbourne, Australia<br>wexlanecafe@mailbrook.com</p>
  </div>
  <div class="abs details">
    <h4>Trading Hours</h4>
    <p>Mon – Fri 5:30am – 4pm<br>Sat 7am – 1pm</p>
  </div>
</section>

</body>
</html>
```